Terra Vibe, mobile, wordpress website

Do you want to directly, and in a big way, create a simple, beautiful, new, innovative lifestyle sports social & mobile site that reflects while grows a emerging community, lifestyle and movement.
A community of not just like-minded individuals and groups, (not just referring to just sports fans, in fact, if you’re not a sports fan, not a big deal) but a community built around numerous shared cultural passions- on and offline.
A site built around not just the universal appeal of sports and celebrity, even celebrity sports fans, but with the potential to become a leader in the transformative movement that’s already begun to shape and drive society and the future. This product, it's informative nature, culture shaping and driving service and community will be as insightful and informative as it will be about entertainment. It will be known for producing and covering big, global events.
Think FUN, irreverent and smart. Think Brevin, Tam Velloza, and a little edgy, like Dirk Wenslow not being completely alienating and bombastic, all sharing funny stuff and thoughts.
Do you want to bring your fresh perspective, while gaining incredible experience, developing key skills, practical knowledge and know how? Bringing to the team your next-generation, Millennial knowledge about the latest mobile technology, and how to most effectively take advantage of this valuable expertise? We know you've got it, and would love what you come up with. Not flashy. Clean, simple background, tons of video displayed in creative, addicting ways. A layout design like http://www.flickcove.example/
The final design should express a site and community that immediately says it's like no other sports site that exists today, while at the same time demonstrating it's where the future of sports is heading.
Updates
Project Deadline Extended
Reason: Due to the Holiday Season, designers demonstrated it was not the best time of year for the contest. We want to give a chance for more designers to participate and designers we are interested in a chance to do modifications.
Target Market(s)
Male 18-34, urban, educated, with disposable income.
Industry/Entity Type
Community
Requirements
Must have
- mobile-optimizing.

```html
<!DOCTYPE html>
<html lang="en">
<head>
<meta charset="utf-8">
<title>Terra Vibe</title>
<link href="https://fonts.googleapis.com/css2?family=Roboto:wght@300;400;500;700&display=swap" rel="stylesheet">
<style>
:root{
  --brand-blue:#1f7fd6;
  --hero-blue:#2b86d3;
  --hero-deep:#1a6cba;
  --hero-light:#5cb8e6;
  --accent-yellow:#ffd200;
  --ink:#222;
  --ink-soft:#555;
  --ink-muted:#888;
  --band-grey:#e9eef4;
  --rule:#d8dde3;
  --white:#fff;
  --bar-blue:#1f7fd6;
  --bar-red:#e0303c;
  --bar-green:#3cc07a;
  --bar-yellow:#f2b51b;
}
*{margin:0;padding:0;box-sizing:border-box}
html,body{width:983px;height:1200px;overflow:hidden;background:var(--white)}
body{position:relative;font-family:"Roboto",Arial,sans-serif;color:var(--ink)}
.abs{position:absolute}

/* header */
.site-header{top:0;left:0;width:983px;height:38px;background:var(--white);border-bottom:1px solid #e3e3e3}
.brand{left:163px;top:8px;font-size:17px;font-weight:500;color:var(--brand-blue)}
.nav-item{top:13px;font-size:10px;color:#444}
.nav-item svg{margin-left:4px;vertical-align:middle}
.search{left:649px;top:12px;font-size:10px;color:#444;display:flex;align-items:center;gap:5px}
.login{left:730px;top:14px;font-size:10px;color:var(--ink-muted)}
.signup{left:770px;top:9px;width:48px;height:20px;background:var(--brand-blue);color:var(--white);font-size:10px;display:flex;align-items:center;justify-content:center;border-radius:2px}

/* hero */
.hero{top:38px;left:0;width:983px;height:214px;
  background:radial-gradient(ellipse 280px 200px at 560px 40px,var(--hero-light),transparent 70%),
             linear-gradient(90deg,var(--hero-deep),var(--hero-blue) 40%,var(--hero-blue) 70%,var(--hero-deep))}
.hero-title{left:0;width:706px;top:42px;text-align:center;font-size:30px;font-weight:700;line-height:36px;color:var(--white)}
.hero-sub{left:0;width:706px;top:84px;text-align:center;font-size:14px;font-weight:500;line-height:18px;color:var(--white)}
.tour-btn{left:262px;top:129px;width:183px;height:37px;background:var(--accent-yellow);color:#222;font-size:13px;font-weight:500;display:flex;align-items:center;justify-content:center;box-shadow:0 2px 3px rgba(0,0,0,.25)}
.hero-video{left:584px;top:35px;width:235px;height:144px;border:3px solid var(--white);box-shadow:0 6px 14px rgba(0,0,0,.3);
  background:linear-gradient(160deg,#b77a6a,#8a4a45 40%,#c9a08c 75%,#6e4036)}
.hero-video svg{position:absolute;left:94px;top:47px}

/* featured */
.section-title{font-size:22px;font-weight:400;color:var(--ink)}
.rule{height:3px;border-top:1px solid var(--rule);border-bottom:1px solid var(--rule)}
.featured-title{left:0;width:983px;top:310px;text-align:center}
.featured-main{left:239px;top:358px;width:505px;height:270px;
  background:linear-gradient(180deg,#d9c2a8,#c89a85 45%,#b8665d 70%,#8a6e5a)}
.featured-caption{left:239px;top:577px;width:505px;height:51px;background:rgba(20,20,20,.72);color:var(--white);padding:11px 13px}
.featured-caption h3{font-size:11px;font-weight:400;margin-bottom:4px}
.featured-caption p{font-size:8px;color:#ddd}

.card{top:660px;width:154px}
.card-bar{height:3px}
.card-img{height:91px;margin-top:4px}
.card h4{font-size:11px;font-weight:400;line-height:13px;margin-top:11px;color:var(--ink)}
.card time{display:block;font-size:8px;color:var(--ink-soft);margin-top:6px}

/* platform band */
.platform{top:852px;left:0;width:983px;height:245px;background:var(--band-grey);border-top:1px solid #dfe4ea;border-bottom:1px solid #d5dbe2}
.platform-title{left:0;width:983px;top:880px;text-align:center;font-size:19px}
.platform-copy{left:188px;top:924px;width:607px;text-align:center;font-size:9.5px;line-height:14px;color:var(--ink-soft)}
.learn-btn{left:413px;top:1014px;width:157px;height:37px;background:var(--white);border:1px solid #999;box-shadow:0 2px 2px rgba(0,0,0,.2);display:flex;align-items:center;justify-content:center;font-size:13px;font-weight:500}

/* footer */
.footer{top:1097px;left:0;width:983px;height:103px;background:linear-gradient(#f4f4f4,var(--white) 40%)}
.legal{left:0;width:983px;top:1119px;text-align:center;font-size:8.5px;color:var(--ink-soft)}
.social{top:1146px;width:22px;height:22px;border-radius:50%;background:#b9b9b9}
</style>
</head>
<body>

<header class="site-header abs">
  <div class="brand abs">Terra Vibe</div>
  <div class="nav-item abs" style="left:310px">Explore<svg width="6" height="4" viewBox="0 0 6 4"><path d="M0.5 0.5L3 3L5.5 0.5" fill="none" stroke="#444" stroke-width="1"/></svg></div>
  <div class="nav-item abs" style="left:370px">Products<svg width="6" height="4" viewBox="0 0 6 4"><path d="M0.5 0.5L3 3L5.5 0.5" fill="none" stroke="#444" stroke-width="1"/></svg></div>
  <div class="search abs"><svg width="11" height="11" viewBox="0 0 11 11"><circle cx="4.5" cy="4.5" r="3.5" fill="none" stroke="#444" stroke-width="1.5"/><path d="M7 7L10 10" stroke="#444" stroke-width="1.8"/></svg>Search</div>
  <div class="login abs">Log in or</div>
  <div class="signup abs">Sign up</div>
</header>

<section class="hero abs">
  <h1 class="hero-title abs">Lorem Ipsum Dolor Sit Amet</h1>
  <p class="hero-sub abs">Excepteur sint occaecat cupidatat non proident sunt in culpa</p>
  <div class="tour-btn abs">TAKE THE TOUR</div>
  <div class="hero-video abs" role="img" aria-label="Video still of a cheering stadium crowd">
    <svg width="44" height="44" viewBox="0 0 44 44"><circle cx="22" cy="22" r="19" fill="none" stroke="rgba(255,255,255,.75)" stroke-width="3"/><path d="M17 13L31 22L17 31Z" fill="rgba(255,255,255,.75)"/></svg>
  </div>
</section>

<div class="rule abs" style="left:240px;top:322px;width:166px"></div>
<h2 class="section-title featured-title abs">Featured shows</h2>
<div class="rule abs" style="left:575px;top:322px;width:169px"></div>

<div class="featured-main abs" role="img" aria-label="Group of friends cheering with raised arms"></div>
<div class="featured-caption abs">
  <h3>Duis aute irure dolor in reprehenderit</h3>
  <p>Excepteur sint occaecat cupidatat non proident, sunt in culpa qui officia deserunt mollit anim id est laborum.</p>
</div>

<article class="card abs" style="left:163px">
  <div class="card-bar" style="background:var(--bar-blue)"></div>
  <div class="card-img" role="img" aria-label="Skier carving down a sunny slope" style="background:linear-gradient(180deg,#2c5fa8,#6d9fd4 55%,#e6eef6)"></div>
  <h4>Lorem ipsum dolor sit amet consectetur adipisicing</h4>
  <time>December 26, 2013</time>
</article>
<article class="card abs" style="left:330px">
  <div class="card-bar" style="background:var(--bar-red)"></div>
  <div class="card-img" role="img" aria-label="Soccer player kicking a ball in a stadium" style="background:linear-gradient(180deg,#3a3f48,#7a6a5e 50%,#5f7a4a)"></div>
  <h4>Lorem ipsum dolor sit amet consectetur adipisicing</h4>
  <time>December 26, 2013</time>
</article>
<article class="card abs" style="left:498px">
  <div class="card-bar" style="background:var(--bar-green)"></div>
  <div class="card-img" role="img" aria-label="Fans raising hands against a blue sky" style="background:linear-gradient(180deg,#a9c4de,#c8d8e6 55%,#c9a18a)"></div>
  <h4>Lorem ipsum dolor sit amet consectetur adipisicing</h4>
  <time>December 26, 2013</time>
</article>
<article class="card abs" style="left:666px">
  <div class="card-bar" style="background:var(--bar-yellow)"></div>
  <div class="card-img" role="img" aria-label="Swimmer racing in a pool lane" style="background:linear-gradient(180deg,#1b4f8f,#2a86c9 50%,#46b0e0)"></div>
  <h4>Lorem ipsum dolor sit amet consectetur adipisicing</h4>
  <time>December 26, 2013</time>
</article>

<section class="platform abs"></section>
<div class="rule abs" style="left:240px;top:892px;width:93px"></div>
<h2 class="section-title platform-title abs">The live video platform you will love</h2>
<div class="rule abs" style="left:650px;top:892px;width:94px"></div>
<p class="platform-copy abs">Lorem ipsum dolor sit amet consectetur adipisicing elit sed do eiusmod tempor incididunt ut labore et dolore magna aliqua. Ut enim ad minim veniam, quis nostrud exercitation ullamco laboris nisi ut aliquip ex ea commodo consequat. Duis aute irure dolor in reprehenderit in voluptate velit esse cillum dolore eu fugiat nulla pariatur. Excepteur sint occaecat cupidatat non proident, sunt in culpa qui officia deserunt mollit anim id est laborum. Lorem ipsum dolor sit amet consectetur adipisicing elit sed do eiusmod tempor incididunt ut labore et dolore magna aliqua. Ut enim ad minim veniam, quis nostrud exercitation ullamco laboris nisi ut aliquip ex ea commodo consequat.</p>
<div class="learn-btn abs">LEARN MORE</div>

<footer class="footer abs"></footer>
<p class="legal abs">© 2013 Terra Vibe, Inc. All rights reserved. / Copyright policy / Privacy policy / Terms of service</p>
<span class="social abs" style="left:440px" aria-label="Social link"></span>
<span class="social abs" style="left:467px" aria-label="Social link"></span>
<span class="social abs" style="left:493px" aria-label="Social link"></span>
<span class="social abs" style="left:519px" aria-label="Social link"></span>

</body>
</html>
```